App Company Business Card Design Project

We are looking for a two sided business card design with one side in English and one side in Chinese. Information should include:
1. Name
2. Email
3. Cell phone
4. Address
Please incorporate the logo attached. Above are the only requirements.

Industry/Entity Type

Business

```html
<!DOCTYPE html>
<html lang="en">
<head>
<meta charset="utf-8">
<title>Kestrel Labs — Business Cards</title>
<link rel="stylesheet" href="https://fonts.googleapis.com/css2?family=Montserrat:wght@600&family=Open+Sans:wght@400;700&family=Noto+Sans+SC:wght@400;500&display=swap">
<style>
  :root {
    --backdrop: #e9e6e1;
    --card: #ffffff;
    --ink: #4a4a4a;
    --green: #5db65a;
    --orange: #f28a5a;
    --teal: #12b7c6;
    --shadow: rgba(0,0,0,0.14);
  }
  * { box-sizing: border-box; margin: 0; padding: 0; }
  html, body { width: 1200px; height: 784px; overflow: hidden; background: var(--backdrop); }
  .sheet { position: relative; width: 1200px; height: 784px; }
  .card {
    position: absolute; width: 540px; height: 310px;
    background: var(--card); box-shadow: 0 8px 22px var(--shadow);
    overflow: hidden; font-family: "Open Sans", sans-serif; color: var(--ink);
  }
  .card--chinese { left: 50px; top: 100px; }
  .card--english { left: 610px; top: 374px; }
  .card__band { position: absolute; inset: 0; }
  .card__corner-art {
    position: absolute; right: 0; top: 40px; width: 180px; height: 270px;
    clip-path: polygon(36% 0, 100% 0, 100% 100%, 66% 100%, 0 48%);
    background: linear-gradient(160deg, var(--orange) 0%, var(--teal) 100%);
  }
  .brand {
    position: absolute; left: 30px; top: 52px;
    display: flex; align-items: center; gap: 12px;
  }
  .brand__dot { width: 26px; height: 26px; border-radius: 50%; background: var(--green); }
  .brand__name {
    font-family: "Montserrat", sans-serif; font-weight: 600;
    font-size: 25px; letter-spacing: 1px; color: var(--ink);
  }
  .holder { position: absolute; left: 30px; top: 142px; }
  .holder__name { font-size: 17px; font-weight: 700; margin-bottom: 10px; letter-spacing: .5px; }
  .card--chinese .holder__name { color: var(--green); font-family: "Noto Sans SC", sans-serif; font-weight: 500; }
  .card--english .holder__name { color: var(--teal); }
  .contact { list-style: none; font-size: 14px; line-height: 19px; }
  .card--chinese .contact { font-family: "Open Sans", "Noto Sans SC", sans-serif; }
  .contact__item { display: flex; align-items: flex-start; gap: 8px; }
  .contact__icon { width: 14px; height: 14px; margin-top: 2px; flex: none; fill: var(--green); }
</style>
</head>
<body>
<main class="sheet">

  <section class="card card--chinese" lang="zh">
    <svg class="card__band" viewBox="0 0 540 310" aria-hidden="true">
      <polygon points="255,0 540,0 540,70 395,140" fill="var(--green)"/>
    </svg>
    <div class="card__corner-art" role="img" aria-label="Large orange and teal geometric brand graphic in the card corner"></div>
    <div class="brand"><span class="brand__dot"></span><span class="brand__name">KESTREL LABS</span></div>
    <div class="holder">
      <p class="holder__name">丹尼尔·任</p>
      <ul class="contact">
        <li class="contact__item"><svg class="contact__icon" viewBox="0 0 16 16"><path d="M3 1l3 3-2 2c1 2 4 5 6 6l2-2 3 3-2 2C7 15 1 9 1 3z"/></svg><span>0400 123 456</span></li>
        <li class="contact__item"><svg class="contact__icon" viewBox="0 0 16 16"><path d="M4 0h8v16H4zM6 2v9h4V2zM7 13h2v1H7z" fill-rule="evenodd"/></svg><span>0400 987 210</span></li>
        <li class="contact__item"><svg class="contact__icon" viewBox="0 0 16 16"><path d="M1 3h14v10H1zM2 4l6 5 6-5z" fill-rule="evenodd"/></svg><span>daniel.wren@kestrellabs.com</span></li>
        <li class="contact__item"><svg class="contact__icon" viewBox="0 0 16 16"><path d="M8 1l7 7h-2v7H9v-4H7v4H3V8H1z"/></svg><span>邮政信箱120街道名称,<br>城市名, 未知</span></li>
      </ul>
    </div>
  </section>

  <section class="card card--english" lang="en">
    <svg class="card__band" viewBox="0 0 540 310" aria-hidden="true">
      <polygon points="255,0 540,0 540,70 395,140" fill="var(--green)"/>
    </svg>
    <div class="card__corner-art" role="img" aria-label="Large orange and teal geometric brand graphic in the card corner"></div>
    <div class="brand"><span class="brand__dot"></span><span class="brand__name">KESTREL LABS</span></div>
    <div class="holder">
      <p class="holder__name">DANIEL WREN</p>
      <ul class="contact">
        <li class="contact__item"><svg class="contact__icon" viewBox="0 0 16 16"><path d="M3 1l3 3-2 2c1 2 4 5 6 6l2-2 3 3-2 2C7 15 1 9 1 3z"/></svg><span>0400 123 456</span></li>
        <li class="contact__item"><svg class="contact__icon" viewBox="0 0 16 16"><path d="M4 0h8v16H4zM6 2v9h4V2zM7 13h2v1H7z" fill-rule="evenodd"/></svg><span>0400 987 210</span></li>
        <li class="contact__item"><svg class="contact__icon" viewBox="0 0 16 16"><path d="M1 3h14v10H1zM2 4l6 5 6-5z" fill-rule="evenodd"/></svg><span>daniel.wren@kestrellabs.com</span></li>
        <li class="contact__item"><svg class="contact__icon" viewBox="0 0 16 16"><path d="M8 1l7 7h-2v7H9v-4H7v4H3V8H1z"/></svg><span>Po box 120 street name,<br>City name, Unknown</span></li>
      </ul>
    </div>
  </section>

</main>
</body>
</html>
```